The Lantern Den Business Cards

We are a Craft Beer/Upscale dining Bar/Restaurant. We'll have 24 taps of craft beers and several types of bottled beers. In addition, we'll be serving a variety of top shelf bourbons, spirits and wines with a small unique menu. I'd like the design to be sophisticated, elegant and modern while staying away from "cartoonish" pictures.
Updates
Hello, I've added some example logos for inspiration. I'd like to use a lot of black/white with maybe a little color for a "pop". Thank you!
Industry/Entity Type
Business
Contact Information for Business Card
THE LANTERN DEN
Tomas Orlikova
582 Wexmoor Street
Norfolk, Virginia 23847
Office: (757) 555-0143
Mobile: (757) 555-0178
Look and feel
Each slider illustrates characteristics of the customer's brand and the style your logo design should communicate.

```html
<!DOCTYPE html>
<html lang="en">
<head>
<meta charset="utf-8">
<title>The Lantern Den — Business Card</title>
<link href="https://fonts.googleapis.com/css2?family=Arimo:wght@400&display=swap" rel="stylesheet">
<style>
  :root {
    --page-bg: #e9e7e3;
    --card-edge: #111111;
    --panel-dark: #141414;
    --panel-mid: #5a5a5a;
    --frame-line: #bdbdbd;
    --paper: #ffffff;
    --ink: #1a1a1a;
    --ink-soft: #444444;
    --brand-ink: #ffffff;
  }
  * { margin: 0; padding: 0; box-sizing: border-box; }
  html, body {
    width: 1200px; height: 800px; overflow: hidden;
    background: var(--page-bg);
  }
  .canvas {
    width: 1200px; height: 800px;
    display: flex; align-items: center; justify-content: center;
  }
  .business-card {
    position: relative;
    width: 1050px; height: 600px;
    background: var(--card-edge);
    padding: 26px;
    box-shadow: 0 18px 40px rgba(0,0,0,0.25);
  }
  .card-frame {
    width: 100%; height: 100%;
    border: 2px solid var(--frame-line);
    padding: 6px;
  }
  .card-inner {
    width: 100%; height: 100%;
    display: flex; flex-direction: column;
  }
  .brand-panel {
    flex: 0 0 46%;
    background: linear-gradient(100deg, var(--panel-dark) 0%, var(--panel-dark) 35%, var(--panel-mid) 100%);
    position: relative;
  }
  .brand {
    position: absolute;
    left: 62%; top: 58%;
    transform: translate(-50%, -50%);
    display: flex; align-items: center; gap: 18px;
    font-family: "Arimo", "Helvetica Neue", Arial, sans-serif;
    font-weight: 400;
    color: var(--brand-ink);
    white-space: nowrap;
  }
  .brand-mark {
    width: 26px; height: 26px;
    border: 2px solid var(--brand-ink);
    flex: none;
  }
  .brand-name { font-size: 38px; font-weight: 400; letter-spacing: 2px; }
  .contact-panel {
    flex: 1;
    background: var(--paper);
    position: relative;
    font-family: "Arimo", "Helvetica Neue", Arial, sans-serif;
    color: var(--ink);
  }
  .person {
    position: absolute;
    left: 90px; top: 42px;
    text-align: right;
  }
  .person-name { font-size: 34px; line-height: 1.1; }
  .person-role { font-size: 17px; color: var(--ink-soft); margin-top: 2px; }
  .divider {
    position: absolute;
    left: 440px; top: 70px;
    width: 2px; height: 92px;
    background: var(--ink);
  }
  .phones {
    position: absolute;
    left: 490px; top: 94px;
    list-style: none;
    font-size: 25px;
    line-height: 1.25;
  }
  .phones li { display: flex; align-items: center; gap: 12px; }
  .phones svg { width: 20px; height: 22px; flex: none; }
  .address {
    position: absolute;
    left: 90px; bottom: 30px;
    font-size: 23px;
    white-space: nowrap;
  }
</style>
</head>
<body>
<main class="canvas">
  <article class="business-card">
    <div class="card-frame">
      <div class="card-inner">
        <header class="brand-panel">
          <div class="brand">
            <span class="brand-mark" aria-hidden="true"></span>
            <h1 class="brand-name">THE LANTERN DEN</h1>
          </div>
        </header>
        <section class="contact-panel">
          <div class="person">
            <p class="person-name">Employee Name</p>
            <p class="person-role">Managing Director</p>
          </div>
          <div class="divider"></div>
          <ul class="phones">
            <li>
              <svg viewBox="0 0 20 22" aria-hidden="true">
                <path d="M2 7 Q10 1 18 7 L16 9 L13 8 L13 6 Q10 5 7 6 L7 8 L4 9 Z" fill="#1a1a1a"/>
                <rect x="4" y="11" width="12" height="9" rx="2" fill="#1a1a1a"/>
                <circle cx="10" cy="15.5" r="2.2" fill="#fff"/>
              </svg>
              <span>(757) 555-0143</span>
            </li>
            <li>
              <svg viewBox="0 0 20 22" aria-hidden="true">
                <rect x="5" y="1" width="10" height="20" rx="2" fill="none" stroke="#1a1a1a" stroke-width="2"/>
                <rect x="7" y="4" width="6" height="6" fill="#1a1a1a"/>
                <circle cx="10" cy="16" r="1.5" fill="#1a1a1a"/>
              </svg>
              <span>(757) 555-0178</span>
            </li>
          </ul>
          <p class="address">Tomas Orlikova 582 Wexmoor Street Norfolk, Virginia 23847</p>
        </section>
      </div>
    </div>
  </article>
</main>
</body>
</html>
```